2-3 Eröffnungsplakate mit Text und Bild
Zielgruppe
Wir verkaufen Industridesign Möbel , Massivholz Tische , Lederstühle und Sitzbänke sowie Loungesessel zu Fabrikpreisen. Zielgruppe ist 25-50 , Stilorientiert und Modebewusst. Individualisten die gerne Ihr Zuhause nicht von der Stange einrichten.
Aufgabenstellung
Wir eröffnen in ca 3 Wochen einen neuen Laden mit unserer Möbel. Der Laden ist direkt an einer viel befahrenen straße. Das Plakat soll für die Neueröffnung werben und eines oder mehrere der angefügten Bilder beinhalten. Die Plakate werden Bauzaungroß also
340cm x 173cm
Es darf nicht viel Text vorkommen, sodass man beim vorbeifahren alles wichtige Lesen kann. Textbeispiele :
- NEUERÖFFNUNG. Massivholztische zu Fabrikpreisen
- NEUERÖFFNUNG. WOHNEN IM LOFT UND INDUSTRIDESIGN ZU HERSTELLERPREISEN
- NEUERÖFFNUNG. Erleben Sie Wohnen im Industrial Design. Einfach und Modern - OHNE ZWISCHENHANDEL DIREKT ZU FABRIKPREISEN
andere Textvorschläge sind erwünscht

```html
<!DOCTYPE html>
<html lang="de">
<head>
<meta charset="utf-8">
<title>Mabrek – Neueröffnung Plakat</title>
<link rel="stylesheet" href="https://fonts.googleapis.com/css2?family=Oswald:wght@400;500;600;700&display=swap">
<style>
  :root {
    --page-bg: #e9eaec;
    --poster-frame: #ffffff;
    --headline-white: #ffffff;
    --accent-yellow: #f2c21b;
    --band-grey: rgba(150, 150, 150, 0.82);
    --brand-ink: #3a3a3a;
    --photo-wall-light: #c9c7c2;
    --photo-wall-dark: #8d8b87;
    --photo-floor: #6f5e4c;
    --photo-wood: #a08665;
  }
  * { margin: 0; padding: 0; box-sizing: border-box; }
  html, body {
    width: 1200px;
    height: 1200px;
    overflow: hidden;
    background: var(--page-bg);
    font-family: "Oswald", "Arial Narrow", sans-serif;
  }
  .canvas {
    position: relative;
    width: 1200px;
    height: 1200px;
    display: flex;
    align-items: center;
    justify-content: center;
  }
  .poster {
    position: relative;
    width: 1120px;
    height: 570px;
    background: var(--poster-frame);
    padding: 12px;
    box-shadow: 0 6px 24px rgba(0,0,0,0.18);
  }
  .poster-inner {
    position: relative;
    width: 100%;
    height: 100%;
    overflow: hidden;
  }
  .scene-photo {
    position: absolute;
    inset: 0;
    background:
      linear-gradient(180deg, rgba(0,0,0,0) 0%, rgba(0,0,0,0) 48%, var(--photo-floor) 70%, #5a4a3b 100%),
      radial-gradient(ellipse at 50% 62%, var(--photo-wood) 0%, rgba(160,134,101,0) 45%),
      linear-gradient(90deg, var(--photo-wall-dark) 0%, var(--photo-wall-light) 35%, var(--photo-wall-light) 65%, var(--photo-wall-dark) 100%);
  }
  .headline {
    position: absolute;
    left: 40px;
    top: 6px;
    display: flex;
    align-items: flex-end;
    line-height: 1;
  }
  .headline-neu {
    font-size: 212px;
    font-weight: 600;
    color: var(--headline-white);
    letter-spacing: -2px;
    line-height: 0.92;
  }
  .headline-eroeffnung {
    font-size: 80px;
    font-weight: 500;
    color: var(--accent-yellow);
    margin-left: 10px;
    margin-bottom: 4px;
  }
  .brand-disc {
    position: absolute;
    right: 18px;
    top: 22px;
    width: 168px;
    height: 168px;
    border-radius: 50%;
    background: #ffffff;
    display: flex;
    align-items: center;
    justify-content: center;
  }
  .brand-name {
    font-size: 40px;
    font-weight: 500;
    color: var(--brand-ink);
    line-height: 1;
  }
  .offer-band {
    position: absolute;
    left: 0;
    right: 0;
    bottom: 0;
    height: 118px;
    background: var(--band-grey);
    display: flex;
    align-items: center;
    padding-left: 40px;
  }
  .offer-main {
    font-size: 80px;
    font-weight: 600;
    color: var(--headline-white);
    letter-spacing: -1px;
    line-height: 1;
  }
  .offer-sub {
    font-size: 42px;
    font-weight: 500;
    color: var(--headline-white);
    margin-left: 12px;
    margin-top: 18px;
    line-height: 1;
  }
  .offer-dot {
    width: 14px;
    height: 14px;
    background: var(--accent-yellow);
    margin-left: 6px;
    margin-top: 40px;
  }
</style>
</head>
<body>
  <main class="canvas">
    <section class="poster">
      <div class="poster-inner">
        <div class="scene-photo" role="img" aria-label="Foto eines Loft-Raums mit Betonwand: Massivholztisch mit Stahlbeinen, Lederstühle und Barhocker mit Ledersitzen"></div>

        <h1 class="headline">
          <span class="headline-neu">NEU</span>
          <span class="headline-eroeffnung">ERÖFFNUNG</span>
        </h1>

        <div class="brand-disc">
          <span class="brand-name">Mabrek</span>
        </div>

        <div class="offer-band">
          <span class="offer-main">MASSIVHOLZTISCHE</span>
          <span class="offer-sub">ZU FABRIKPREISEN</span>
          <span class="offer-dot"></span>
        </div>
      </div>
    </section>
  </main>
</body>
</html>
```